Need A Standard Musical Download Website

We are looking for a talented designer to create a unique web design for our startup Music website called Vorlen Music.
The website should be responsive and filled with some creative stuffs along with bright colors.

Vorlen music is a website loaded with different types of music and capable of downloading the requested music by its users.
There will be categories of music which would be sorted by the genre. They include RnB, Hip-Hop, Afro pop, Pop, Dancehall and Reggae).

DESIGN STYLE/THEME

Creative, trendy, colorful, unique, and easy to use. You have freedom of selecting which ever color suits you. The design must be energetic and attractive.

NAVIGATION

HOME-MUSIC(RnB, Hip hop, Afro pop, POP, dancehall, Reggae)-ARTISTE-NEWS-LOGIN

PAGES REQUIRED
------------
1)Home Page
2)Music

FONTS
GOOGLE FONTS is strongly recommended.

Designers can get inspiration from https://tunebarrowk.com

Industry/Entity Type

Startup

```html
<!DOCTYPE html>
<html lang="en">
<head>
<meta charset="utf-8">
<title>Vorlen Music</title>
<link href="https://fonts.googleapis.com/css2?family=Source+Sans+3:wght@400;600;700&display=swap" rel="stylesheet">
<style>
:root{
  --ink:#2b2b2b;
  --muted:#6d6d6d;
  --white:#ffffff;
  --line:#cfcfcf;
  --blue:#3aa6e6;
  --blue-soft:#8ccbf0;
  --footer:#232323;
  --footer-text:#a8a8a8;
  --footer-accent:#4fb0e8;
}
*{margin:0;padding:0;box-sizing:border-box}
html,body{width:1200px;height:4332px;overflow:hidden}
body{font-family:"Source Sans 3",Arial,sans-serif;color:var(--ink);background:var(--white);position:relative}
.abs{position:absolute}
.photo{position:absolute;left:0;width:1200px}

/* hero */
.hero{top:0;height:800px;background:radial-gradient(ellipse at 30% 35%,#7fe6e0 0%,#1f9fa7 22%,#0f4f63 48%,#0a1c28 80%)}
.nav-brand{left:40px;top:26px;font-size:34px;font-weight:600;color:var(--white)}
.nav{right:40px;top:32px;display:flex;gap:44px}
.nav a{color:var(--white);text-decoration:none;font-size:19px;letter-spacing:1px}
.nav a.active{border-bottom:2px solid var(--white);padding-bottom:4px}
.hero-title{left:0;width:1200px;top:170px;text-align:center;color:var(--white);font-size:50px;font-weight:600;line-height:1.15}
.btn-ghost{border:2px solid var(--white);color:var(--white);font-size:17px;letter-spacing:1px;text-align:center;line-height:52px;height:56px}

/* intro */
.intro{left:150px;top:830px;width:900px;text-align:center;font-size:19px;line-height:1.35;color:var(--ink)}
.topic{top:970px;width:260px;text-align:center}
.topic svg{display:block;margin:0 auto}
.topic h3{font-size:21px;font-weight:700;margin-top:14px}
.topic p{font-size:18px;color:var(--muted);margin-top:4px}

/* browse */
.browse{top:1260px;height:780px;clip-path:polygon(0 70px,1200px 0,1200px 780px,0 780px);background:linear-gradient(180deg,#3e4a7a 0%,#6a4a7e 35%,#8d5a6a 60%,#3b3450 100%)}
.sec-title{left:0;width:1200px;text-align:center;color:var(--white);font-weight:700;font-size:40px}
.genre{width:240px;height:52px;border:2px solid var(--white);color:var(--white);text-align:center;line-height:48px;font-size:17px;font-weight:600;letter-spacing:1px}

/* tracks */
.tracks{top:1960px;height:680px;clip-path:polygon(0 0,1200px 80px,1200px 600px,0 680px);background:linear-gradient(135deg,#0c1d3a 0%,#1a4f8a 40%,#2fa0d8 62%,#0b2447 100%)}
.para{left:190px;width:820px;text-align:center;color:var(--white);font-size:19px;line-height:1.3}

/* anywhere */
.anywhere{top:2560px;height:680px;clip-path:polygon(0 80px,1200px 0,1200px 680px,0 680px);background:linear-gradient(160deg,#bfe6e0 0%,#e8efe4 40%,#d9c6a6 70%,#a9d3d6 100%)}
.dark-title{color:#1f1f1f}
.dark-para{color:#222}

/* pricing */
.plan{text-align:center}
.plan h3{font-size:32px;font-weight:600;margin-top:34px}
.plan ul{list-style:none;margin-top:34px;font-size:18px;line-height:2.1}
.plan .btn{position:absolute;left:50%;transform:translateX(-50%);bottom:34px;width:240px;height:54px;line-height:50px;font-size:17px;letter-spacing:1px}
.plan-starter{left:100px;top:3392px;width:320px;height:368px;border:2px solid #bfe1f5;background:var(--white);color:var(--blue-soft)}
.plan-starter h3{color:var(--blue)}
.plan-starter .btn{border:2px solid var(--blue-soft);color:var(--blue)}
.plan-basic{left:448px;top:3340px;width:312px;height:480px;background:linear-gradient(180deg,#f5e83a 0%,#7fd35a 45%,#1fb3a6 100%);color:var(--white)}
.plan-pro{left:788px;top:3300px;width:312px;height:580px;background:linear-gradient(180deg,#8a2fa8 0%,#5a58c8 45%,#1fb8b0 100%);color:var(--white)}
.plan-basic .btn,.plan-pro .btn{border:2px solid var(--white);color:var(--white)}

/* footer */
.footer{top:3980px;height:352px;background:var(--footer)}
.foot-brand{left:100px;top:4020px;font-size:30px;font-weight:600;color:var(--white)}
.foot-links{left:100px;top:4075px;list-style:none;font-size:17px;line-height:2.05;color:var(--footer-text)}
.foot-contact{right:100px;top:4020px;text-align:right;font-size:17px;line-height:1.55;color:var(--footer-text)}
.foot-contact h4{color:var(--footer-accent);font-size:19px;font-weight:600;margin-bottom:6px}
.foot-contact .gap{margin-top:18px}
</style>
</head>
<body>

<section class="photo hero" role="img" aria-label="Concert crowd under teal stage lights with hands forming a heart"></section>
<div class="abs nav-brand">Vorlen Music</div>
<nav class="abs nav">
  <a class="active" href="#">CATEGORIES</a><a href="#">BLOG</a><a href="#">CONTACT</a><a href="#">LOGIN</a>
</nav>
<h1 class="abs hero-title">All the music you love and<br>all the music you will love</h1>
<a class="abs btn-ghost" style="left:480px;top:592px;width:240px">START MY JOURNEY</a>

<p class="abs intro">"Lorem ipsum dolor sit amet, consectetur adipiscing elit, sed do eiusmod tempor incididunt ut labore et dolore magna aliqua. Ut enim ad minim veniam, quis nostrud exercitation ullamco laboris nisi ut aliquip ex ea commodo consequat. Duis aute irure dolor in reprehenderit in voluptate velit esse cillum dolore eu fugiat nulla pariatur. Excepteur sint occaecat cupidatat non proident, sunt in culpa qui officia deserunt mollit anim id est laborum."</p>

<div class="abs topic" style="left:110px">
  <svg width="120" height="190" viewBox="0 0 120 190" fill="none" stroke="#555" stroke-width="3"><rect x="8" y="4" width="104" height="182" rx="12"/><line x1="8" y1="30" x2="112" y2="30"/><line x1="8" y1="158" x2="112" y2="158"/><circle cx="42" cy="94" r="16"/><rect x="64" y="84" width="32" height="20"/></svg>
  <h3>Sample Topic</h3><p>Some more text below</p>
</div>
<div class="abs topic" style="left:470px">
  <svg width="120" height="190" viewBox="0 0 120 190" fill="none" stroke="#555" stroke-width="3"><rect x="8" y="4" width="104" height="182" rx="12"/><line x1="8" y1="30" x2="112" y2="30"/><line x1="8" y1="158" x2="112" y2="158"/><circle cx="42" cy="94" r="16"/><rect x="64" y="84" width="32" height="20"/></svg>
  <h3>Sample Topic</h3><p>Some more text below</p>
</div>
<div class="abs topic" style="left:830px">
  <svg width="120" height="190" viewBox="0 0 120 190" fill="none" stroke="#555" stroke-width="3"><rect x="8" y="4" width="104" height="182" rx="12"/><line x1="8" y1="30" x2="112" y2="30"/><line x1="8" y1="158" x2="112" y2="158"/><circle cx="42" cy="94" r="16"/><rect x="64" y="84" width="32" height="20"/></svg>
  <h3>Sample Topic</h3><p>Some more text below</p>
</div>

<section class="photo browse" role="img" aria-label="Large festival crowd in front of a stage"></section>
<h2 class="abs sec-title" style="top:1455px">Browse the entire library of music today</h2>
<a class="abs genre" style="left:232px;top:1556px">HIP - HOP</a>
<a class="abs genre" style="left:668px;top:1556px">POP</a>
<a class="abs genre" style="left:232px;top:1666px">R&amp;B</a>
<a class="abs genre" style="left:668px;top:1666px">DANCEHALL</a>
<a class="abs genre" style="left:232px;top:1776px">REGGAE</a>
<a class="abs genre" style="left:668px;top:1776px">AFRO - POP</a>

<section class="photo tracks" role="img" aria-label="DJ hands on a mixing deck in blue light"></section>
<h2 class="abs sec-title" style="top:2085px">Over 5,000,000 tracks and brand new mixes</h2>
<p class="abs para" style="top:2176px">"Lorem ipsum dolor sit amet, consectetur adipiscing elit, sed do eiusmod tempor incididunt ut labore et dolore magna aliqua. Ut enim ad minim veniam, quis nostrud exercitation ullamco laboris nisi ut aliquip ex ea commodo consequat. Duis aute irure dolor in reprehenderit in voluptate velit esse cillum dolore eu fugiat nulla pariatur. Excepteur sint occaecat cupidatat non proident, sunt in culpa qui officia deserunt mollit anim id est laborum."</p>
<a class="abs btn-ghost" style="left:480px;top:2412px;width:240px">LEARN MORE</a>

<section class="photo anywhere" role="img" aria-label="Woman with headphones enjoying music outdoors in sunlight"></section>
<h2 class="abs sec-title dark-title" style="top:3040px">The music you love, wherever you go</h2>
<p class="abs para dark-para" style="top:3098px">"Lorem ipsum dolor sit amet, consectetur adipiscing elit, sed do eiusmod tempor incididunt ut labore et dolore magna aliqua. Ut enim ad minim veniam, quis nostrud exercitation ullamco laboris nisi ut aliquip ex ea commodo consequat. Duis aute irure dolor in reprehenderit in voluptate velit esse cillum dolore eu fugiat nulla pariatur."</p>

<div class="abs plan plan-starter">
  <h3>STARTER</h3>
  <ul><li>Listen to unlimited music</li><li>Download 100 tracks</li><li>24 hour support</li></ul>
  <a class="btn">LEARN MORE</a>
</div>
<div class="abs plan plan-basic">
  <h3>BASIC</h3>
  <ul><li>Listen to unlimited music</li><li>Download 500 tracks</li><li>24 hour support</li><li>Stream on all devices</li><li>Make unlimited playlists</li></ul>
  <a class="btn">LEARN MORE</a>
</div>
<div class="abs plan plan-pro">
  <h3>PRO</h3>
  <ul><li>Listen to unlimited music</li><li>Download all tracks</li><li>24 hour support</li><li>Stream on all devices</li><li>Make unlimited playlists</li><li>Share music with friends</li><li>Exclusive new mixes</li></ul>
  <a class="btn">LEARN MORE</a>
</div>

<footer class="photo footer"></footer>
<div class="abs foot-brand">Vorlen Music</div>
<ul class="abs foot-links">
  <li>Privacy Policy</li><li>Terms and Conditions</li><li>Disclaimer</li><li>Site Map</li><li>About Us</li>
</ul>
<div class="abs foot-contact">
  <h4>Contact Us</h4>
  <p>Address line 01</p><p>Address line 02</p><p>City, State</p><p>Postal Code</p>
  <p class="gap">+011 555 01420</p><p>hello@vorlenmusic.com</p>
</div>

</body>
</html>
```